Business Card Design for Tax Accounting Company

I need design files that can be edited to add new professional designations onto the end of my name once complete. I need design files that can be edited for new employees. I also need the design files to be able to upload into CardNest for new orders. I've attached multiple logo files with varying file extensions to help with the design.
Please include the following contact information:
Marcus Tellan, CFP®, EA, CTC, CEPA
Founder & CEO
C (480) 517.3082
F (623) 389.5170
718 W Larkspur Ave
Mesa, AZ 85210
Updates
I need the business card to include the following contact info:
C: (480)517.3082
F: (623) 389.5170
mt@RidgewayLedgerGroup.com
www.MarcusRTellan.com
Address to be included is
718 W Larkspur Ave
Mesa, AZ 85210
Business Cards are double sided
Target Market(s)
Business owners $1M+ annual revenue, especially for the construction and technology industries
Industry/Entity Type
Accounting & Tax
Contact Information for Business Card
Contact information and logo
Look and feel
Each slider illustrates characteristics of the customer's brand and the style your logo design should communicate.

```html
<!DOCTYPE html>
<html lang="en">
<head>
<meta charset="utf-8">
<title>Ridgeway Ledger Group – Business Card</title>
<link href="https://fonts.googleapis.com/css2?family=Source+Serif+4:wght@400;600;700&display=swap" rel="stylesheet">
<style>
  :root {
    --backdrop: #000000;
    --card: #ffffff;
    --navy: #0b2361;
    --crimson: #bf0d32;
    --sun: #fcd800;
    --copper: #d05f17;
  }
  html, body {
    margin: 0;
    width: 1200px;
    height: 1200px;
    overflow: hidden;
    background: var(--backdrop);
    font-family: "Source Serif 4", Georgia, serif;
  }
  .stage { position: relative; width: 1200px; height: 1200px; }
  .card {
    position: absolute;
    width: 769px;
    height: 497px;
    background: var(--card);
    overflow: hidden;
  }
  .card--front { left: 73px; top: 70px; }
  .card--back { left: 361px; top: 618px; }

  .brand {
    position: absolute;
    display: flex;
    flex-direction: column;
    align-items: center;
    text-align: center;
  }
  .brand__mark {
    border-radius: 50%;
    background: var(--crimson);
  }
  .brand__name {
    color: var(--navy);
    font-weight: 700;
    line-height: 1.05;
  }
  .card--front .brand { left: 234px; top: 116px; width: 300px; }
  .card--front .brand__mark { width: 150px; height: 150px; margin-bottom: 24px; }
  .card--front .brand__name { font-size: 34px; }

  .card--back .brand { left: 104px; top: 146px; width: 240px; }
  .card--back .brand__mark { width: 110px; height: 110px; margin-bottom: 18px; }
  .card--back .brand__name { font-size: 26px; }

  .person { position: absolute; left: 411px; top: 140px; }
  .person__name {
    margin: 0;
    color: var(--crimson);
    font-size: 27px;
    font-weight: 700;
    line-height: 1;
  }
  .person__title {
    margin: 8px 0 0;
    color: var(--crimson);
    font-size: 15px;
    font-weight: 400;
  }
  .contact {
    list-style: none;
    margin: 30px 0 0;
    padding: 0;
  }
  .contact__item {
    display: flex;
    align-items: center;
    height: 27.5px;
    color: var(--navy);
    font-size: 15.5px;
  }
  .contact__icon { width: 16px; height: 16px; margin-right: 11px; flex: none; }

  .web-band {
    position: absolute;
    left: 0; right: 0; bottom: 0;
    height: 39px;
    background: var(--sun);
    display: flex;
    align-items: center;
    justify-content: center;
    color: var(--navy);
    font-size: 14px;
    font-weight: 700;
    letter-spacing: 0.3px;
  }
</style>
</head>
<body>
<div class="stage">

  <section class="card card--front">
    <div class="brand">
      <div class="brand__mark"></div>
      <div class="brand__name">Ridgeway Ledger Group</div>
    </div>
  </section>

  <section class="card card--back">
    <div class="brand">
      <div class="brand__mark"></div>
      <div class="brand__name">Ridgeway Ledger Group</div>
    </div>

    <div class="person">
      <h1 class="person__name">Marcus Tellan</h1>
      <p class="person__title">(CFP®, EA, CTC, CEPA, Founder &amp; CEO)</p>
      <ul class="contact">
        <li class="contact__item">
          <svg class="contact__icon" viewBox="0 0 16 16"><rect x="4" y="1" width="8" height="14" rx="1.5" fill="none" stroke="#bf0d32" stroke-width="1.4"/><line x1="7" y1="12.5" x2="9" y2="12.5" stroke="#bf0d32" stroke-width="1.2"/></svg>
          (480) 517.3082
        </li>
        <li class="contact__item">
          <svg class="contact__icon" viewBox="0 0 16 16"><rect x="4" y="1.5" width="8" height="4" fill="none" stroke="#bf0d32" stroke-width="1.3"/><rect x="1.5" y="5.5" width="13" height="6" rx="1" fill="none" stroke="#bf0d32" stroke-width="1.3"/><rect x="4" y="9" width="8" height="5.5" fill="#fff" stroke="#bf0d32" stroke-width="1.3"/></svg>
          (623) 389.5170
        </li>
        <li class="contact__item">
          <svg class="contact__icon" viewBox="0 0 16 16"><rect x="1" y="3.5" width="14" height="9" fill="#bf0d32"/><polyline points="1.5,4 8,9 14.5,4" fill="none" stroke="#fff" stroke-width="1.1"/></svg>
          mt@RidgewayLedgerGroup.com
        </li>
        <li class="contact__item">
          <svg class="contact__icon" viewBox="0 0 16 16"><path d="M8 1a5 5 0 0 0-5 5c0 3.6 5 9 5 9s5-5.4 5-9a5 5 0 0 0-5-5z" fill="#bf0d32"/><circle cx="8" cy="6" r="1.9" fill="#fff"/></svg>
          718 W Larkspur Ave Mesa, AZ 85210
        </li>
      </ul>
    </div>

    <div class="web-band">www.MarcusRTellan.com</div>
  </section>

</div>
</body>
</html>
```